Flyer DL double sided Design Project

Hi,

Our company Marlow Panels makes kitchen and wardrobe doors. I would like an attractive and sales focused artwork for a DL flyer for general promotional use to be printed and also emailed to customers. The flyer will be a double sided, full colour and gloss finish.

We would hand out this flyer to people wanting to replace their old kitchen doors with new ones. The flyer is aimed at the general public and the Do It Yourself market as we supply the doors only, we don't measure or install.

Text will be provided but here are some guidelines:

Headline: IS YOUR KITCHEN IN NEED OF A MAKEOVER? JUST REPLACE THE DOORS SAVING YOU THOUSANDS OF $$$

This month’s special offers: Online orders only. ORDER NOW! (icon)

5 reasons to replace kitchen doors compared to a full kitchen renovation:
1. Its cheaper text, text, text
2. It's quicker text, text, text
3. It's easier text, text, text
4. It's less hassle and mess text, text, text
5. It's less wastage text, text, text

I can also provide a few high quality images of kitchens.

Reason: I won't be available to provide feedback on the design and finalise it within the deadline date. Regards, Brenda

Reason: I don't have the wording and final image today. I will be able to finalise early next week.

Target Market(s)

DO IT YOURSELF - DIY
This is mainly aimed at people who want to replace their kitchen doors themselves. People interested in improving the value of their home and saving a lot of money on their kitchen renovation.
Home owners - usually adults in the 30-50 year age bracket.

Industry/Entity Type

It Company

Requirements
Must have
• List our website www.marlowpanels.com.au
List our email address: sales@marlowpanels.com.au
We do not measure or install. We can give quotes to customers who email a list of door sizes to us. For example: Headline: Get a quote now! Smaller print: Download a quote form (from our website www.marlowpanels.com.au) and send your door sizes for a quote today!
Nice to have
• Promotion: Order now and receive free delivery (on orders over $1000). Sydney metro area. Limited time only.
I like the design done by Quartzfern41 with "We do wardrobe doors too" on the back of the flyer.
Delivery to your door anywhere in Australia.

```html
<!DOCTYPE html>
<html lang="en">
<head>
<meta charset="utf-8">
<title>Marlow Panels – DL Flyer</title>
<link href="https://fonts.googleapis.com/css2?family=Arimo:wght@400;700&display=swap" rel="stylesheet">
<style>
  :root{
    --stage:#2e2522;
    --paper:#ffffff;
    --ink:#1a1a1a;
    --orange:#f6b94f;
    --orange-pale:#f7d9a6;
    --door-red:#c8202a;
    --door-red-dark:#8e1119;
    --panel-grey:#dfe3e2;
    --panel-cream:#f3efe4;
    --badge-blue:#1d3f8f;
  }
  *{box-sizing:border-box;margin:0;padding:0}
  html,body{width:1200px;height:900px;overflow:hidden}
  body{background:var(--stage);font-family:"Arimo",Arial,sans-serif;color:var(--ink);position:relative}

  .flyer{position:absolute;top:70px;width:355px;height:760px;background:var(--paper);overflow:hidden}
  .flyer--back{left:235px}
  .flyer--front{left:610px}

  /* back side */
  .hero-image{position:absolute;left:0;top:0;width:100%;height:270px;
    background:linear-gradient(160deg,var(--panel-cream) 0%,var(--panel-grey) 55%,#c9cfcd 100%)}
  .brand-title{position:absolute;left:18px;top:36px;font-size:43px;font-weight:700;letter-spacing:-.5px}
  .brand-tag{position:absolute;left:34px;top:94px;font-size:22px;font-weight:700}
  .saving-head{position:absolute;left:0;top:212px;width:100%;text-align:center;font-size:17px;font-weight:700;line-height:1.2}
  .reasons-intro{position:absolute;left:0;top:276px;width:100%;text-align:center;font-size:15px;font-weight:700;line-height:1.2}
  .reasons{position:absolute;left:26px;top:322px;list-style:none;font-size:18px;font-weight:700;line-height:1.2}
  .quality-badge{position:absolute;right:14px;top:332px}
  .quote-head{position:absolute;left:0;top:470px;width:100%;text-align:center;font-size:27px;font-weight:700}
  .quote-copy{position:absolute;left:0;top:506px;width:100%;text-align:center;font-size:11px;font-weight:700;line-height:1.3}
  .order-now{position:absolute;left:0;top:566px;width:100%;text-align:center;font-size:17px;font-weight:700}
  .promo-head{position:absolute;left:0;top:612px;width:100%;text-align:center;font-size:21px;font-weight:700}
  .promo-copy{position:absolute;left:0;top:640px;width:100%;text-align:center;font-size:11px;line-height:1.3}
  .promo-copy strong{display:block;font-weight:700}
  .disclaimer{position:absolute;left:0;top:708px;width:100%;text-align:center;font-size:9px}
  .site-url{position:absolute;left:0;bottom:14px;width:100%;text-align:center;font-size:15px;font-weight:700;letter-spacing:4px}

  /* front side */
  .wave{position:absolute;left:0;top:0}
  .brand-mark{position:absolute;left:14px;top:30px;width:112px;display:flex;flex-direction:column;align-items:flex-start;gap:8px}
  .brand-mark__square{width:22px;height:22px;background:var(--ink)}
  .brand-mark__name{font-size:24px;font-weight:700;line-height:1.05}
  .collection{position:absolute;left:140px;top:70px;color:var(--orange-pale);font-weight:700}
  .collection__big{font-size:35px;display:block}
  .collection__small{font-size:24px;font-weight:400;display:block;margin-top:2px}
  .offers{position:absolute;left:0;top:228px;width:100%;text-align:center;font-size:17px;font-weight:700}
  .headline{position:absolute;left:30px;top:282px;width:290px;text-align:center;font-size:26px;font-weight:700;line-height:1.3}
  .door-image{position:absolute;right:0;top:360px}
  .contact{position:absolute;left:20px;top:535px;width:260px;text-align:center;font-weight:700}
  .contact__name{font-size:19px}
  .contact__addr{font-size:14px;line-height:1.25}
  .contact__lines{margin-top:42px;font-size:14px;line-height:1.25}
</style>
</head>
<body>

<section class="flyer flyer--back" aria-label="Flyer back side">
  <div class="hero-image" role="img" aria-label="Illustration of white wardrobe and cabinet door panels"></div>
  <h1 class="brand-title">Marlow Panels</h1>
  <p class="brand-tag">We do wardrobe doors too</p>
  <p class="saving-head">JUST REPLACE THE DOORS<br>SAVING YOU THOUSANDS OF $$$</p>
  <p class="reasons-intro">5 Reasons to replace kitchen doors<br>compared to a full kitchen renovation:</p>
  <ol class="reasons">
    <li>1. Its cheaper</li>
    <li>2. Its quicker</li>
    <li>3. Its easier</li>
    <li>4. Its less hassle and mess</li>
    <li>5. Its less wastage</li>
  </ol>
  <svg class="quality-badge" width="62" height="62" viewBox="0 0 78 78" aria-hidden="true">
    <circle cx="39" cy="39" r="37" fill="var(--badge-blue)"/>
    <circle cx="39" cy="39" r="26" fill="#fff"/>
  </svg>
  <h2 class="quote-head">Get a quote now!</h2>
  <p class="quote-copy">Download a quote form from our website<br>www.marlowpanels.com.au<br>and send your door sizes for a quote today!</p>
  <p class="order-now">Online orders only. ORDER NOW!</p>
  <h2 class="promo-head">Promotion</h2>
  <p class="promo-copy">Order now and receive free delivery<br>(on orders over $1000). Sydney metro area.<br>Limited time only.<strong>Delivery to your door anywhere in Australia.</strong></p>
  <p class="disclaimer">*We do not measure or install.</p>
  <p class="site-url">www.marlowpanels.com.au</p>
</section>

<section class="flyer flyer--front" aria-label="Flyer front side">
  <svg class="wave" width="355" height="760" viewBox="0 0 355 760" aria-hidden="true">
    <path d="M0 0 H128 C150 120 40 200 55 330 C70 470 150 560 120 760 H0 Z" fill="var(--orange)"/>
  </svg>
  <div class="brand-mark">
    <span class="brand-mark__square"></span>
    <span class="brand-mark__name">Marlow Panels</span>
  </div>
  <p class="collection"><span class="collection__big">ultimate</span><span class="collection__small">door collection</span></p>
  <p class="offers">This month’s special offers:</p>
  <h2 class="headline">IS YOUR KITCHEN<br>IN NEED<br>OF A<br>MAKEOVER?</h2>
  <svg class="door-image" width="150" height="320" viewBox="0 0 150 320" role="img" aria-label="Photo of a red kitchen cabinet door">
    <defs>
      <linearGradient id="doorShade" x1="0" y1="0" x2="1" y2="1">
        <stop offset="0" stop-color="var(--door-red)"/>
        <stop offset="1" stop-color="var(--door-red-dark)"/>
      </linearGradient>
    </defs>
    <polygon points="0,90 150,0 150,320 120,320" fill="url(#doorShade)"/>
  </svg>
  <div class="contact">
    <p class="contact__name">MARLOW PANELS</p>
    <p class="contact__addr">14 Harlow Street,<br>Kingsgrove NSW 2208</p>
    <p class="contact__lines">Ph 9480 3312<br>Fax 9480 3319<br>Email sales@marlowpanels.com.au</p>
  </div>
  <p class="site-url">www.marlowpanels.com.au</p>
</section>

</body>
</html>
```